Lucky Ridge Game Evenings Business Card Design

I need a business card for a fun casino entertainment business. I would like one side of the business card to convey the feel of a playing card similar to the playing card uploaded but with one logo placed horizontally across the card and the web address below it.
the information side can be slightly more plain, maybe just a stack of chips along one side or something with a casino feel.

Industry/Entity Type

Casino

Contact Information for Business Card

Lucky Ridge Game Evenings
Dev Marrowby
Director
0452 618290
dev@luckyridgefun.com.au

```html
<!DOCTYPE html>
<html lang="en">
<head>
<meta charset="utf-8">
<title>Lucky Ridge Game Evenings – Business Card</title>
<link rel="stylesheet" href="https://fonts.googleapis.com/css2?family=Oswald:wght@500;700&family=Libre+Baskerville&family=Kaushan+Script&display=swap">
<style>
  :root {
    --page-bg: #f2f2f2;
    --felt-green: #3f9462;
    --felt-dark: #2f7a4d;
    --felt-light: #55a875;
    --gold: #f2b92c;
    --card-white: #ffffff;
    --ink: #1e1e1e;
    --ink-soft: #444444;
    --chip-ghost: #f1f1f1;
    --web-light: #eaf4ee;
  }
  * { margin: 0; padding: 0; box-sizing: border-box; }
  html, body {
    width: 1200px; height: 1000px; overflow: hidden;
    background: var(--page-bg);
  }
  .sheet {
    width: 1200px; height: 1000px;
    display: flex; flex-direction: column;
    align-items: center; justify-content: center; gap: 56px;
  }
  .card {
    position: relative;
    width: 740px; height: 420px;
    border-radius: 26px;
    overflow: hidden;
    box-shadow: 0 6px 18px rgba(0,0,0,0.12);
  }

  /* Front side */
  .card--front { background: var(--felt-green); }
  .front__pattern {
    position: absolute; inset: 0;
    background: radial-gradient(ellipse at center, var(--felt-light) 0%, var(--felt-green) 55%, var(--felt-dark) 100%);
  }
  .front__brand {
    position: absolute; inset: 0;
    display: flex; align-items: center; justify-content: center; gap: 14px;
  }
  .front__brand-dot {
    width: 34px; height: 34px; border-radius: 50%;
    background: var(--gold);
    flex: none;
  }
  .front__brand-name {
    font-family: 'Oswald', sans-serif;
    font-weight: 700;
    font-size: 42px;
    letter-spacing: 1px;
    color: var(--gold);
    white-space: nowrap;
  }
  .front__web {
    position: absolute;
    right: 20px; bottom: 32px;
    writing-mode: vertical-rl;
    transform: rotate(180deg);
    font-family: 'Libre Baskerville', serif;
    font-size: 17px;
    line-height: 1;
    color: var(--web-light);
    letter-spacing: 0.5px;
    white-space: nowrap;
  }

  /* Back side */
  .card--back { background: var(--card-white); }
  .back__chips {
    position: absolute; left: 300px; top: 90px;
    width: 180px; height: 240px;
    border-radius: 16px;
    background: var(--chip-ghost);
  }
  .corner {
    position: absolute;
    display: flex; align-items: center; gap: 6px;
    font-family: 'Libre Baskerville', serif;
    font-size: 46px; line-height: 1; color: var(--ink);
  }
  .corner svg { width: 36px; height: 40px; }
  .corner--top { left: 40px; top: 150px; }
  .corner--bottom { right: 40px; bottom: 150px; transform: rotate(180deg); }
  .back__details {
    position: absolute; left: 0; right: 0; top: 72px;
    text-align: center;
  }
  .back__company {
    font-family: 'Kaushan Script', cursive;
    font-size: 30px; line-height: 1.2; color: var(--ink);
  }
  .back__name {
    margin-top: 30px;
    font-family: 'Oswald', sans-serif;
    font-weight: 700; font-size: 34px; line-height: 1.1;
    color: var(--ink); letter-spacing: 1px;
    text-transform: uppercase;
  }
  .back__role {
    margin-top: 4px;
    font-family: 'Libre Baskerville', serif;
    font-size: 15px; color: var(--ink-soft);
  }
  .back__contact {
    margin-top: 24px;
    list-style: none;
    font-family: 'Libre Baskerville', serif;
    font-size: 16px; line-height: 1.65;
    color: var(--ink-soft);
  }
</style>
</head>
<body>
<main class="sheet">

  <section class="card card--front">
    <div class="front__pattern" role="img" aria-label="Green felt background with halftone dots and radiating rays"></div>
    <div class="front__brand">
      <span class="front__brand-dot"></span>
      <span class="front__brand-name">Lucky Ridge Game Evenings</span>
    </div>
    <p class="front__web">www.luckyridgefun.com.ua</p>
  </section>

  <section class="card card--back">
    <div class="back__chips" role="img" aria-label="Faint stack of casino chips behind the details"></div>

    <div class="corner corner--top">
      <span>A</span>
      <svg viewBox="0 0 36 40" aria-hidden="true">
        <path d="M18 2 C10 12 2 17 2 25 C2 31 8 34 13 31 C14 30 15 29 16 28 C15 33 13 36 10 38 L26 38 C23 36 21 33 20 28 C21 29 22 30 23 31 C28 34 34 31 34 25 C34 17 26 12 18 2 Z" fill="currentColor"/>
      </svg>
    </div>
    <div class="corner corner--bottom">
      <span>A</span>
      <svg viewBox="0 0 36 40" aria-hidden="true">
        <path d="M18 2 C10 12 2 17 2 25 C2 31 8 34 13 31 C14 30 15 29 16 28 C15 33 13 36 10 38 L26 38 C23 36 21 33 20 28 C21 29 22 30 23 31 C28 34 34 31 34 25 C34 17 26 12 18 2 Z" fill="currentColor"/>
      </svg>
    </div>

    <div class="back__details">
      <p class="back__company">Lucky Ridge Game Evenings</p>
      <h1 class="back__name">Dev Marrowby</h1>
      <p class="back__role">director</p>
      <ul class="back__contact">
        <li>phone: 0452 618290</li>
        <li>dev@luckyridgefun.com.au</li>
        <li>www.luckyridgefun.com.ua</li>
      </ul>
    </div>
  </section>

</main>
</body>
</html>
```